"The Wandering Mentor", a Higher Ed blogger, would like a wordpress design

I would like a wordpress design for blogs written by "The Wandering Mentor." that can be easily expanded by me once the initial design is complete.

Here is context which I would like included on the Home/Welcome page: "I started The Wandering Mentor in 2021 to write about the practice of academic advising through the lens of horsemanship. After one year of developing skills as a brand new equestrian, I couldn’t help but notice the similarities between my vocation as an academic advisor and my avocation as a budding equestrian. I hope my musings about my journey in two very different fields will cultivate curiosity, widen your aperture and ignite academic advisors to take their practice to the next level. "

The wordpress will primarily have blogs by myself or guest bloggers writing about academic advising for advisors, but I may widen my audience to include students and families. I'd like to have readers submit questions that I can answer. Depending on interest, I may want to have a section on Horsemanship but that is not truly the focus of this site.

I'd like the feel of the site to be positive, fresh, modern (but not too wild), with the emphasis on Higher Ed/Academic Advising as opposed to equestrian pursuits. I don't want it to feel clunky and blocky like some sites that have to do with education. I'm hoping that readers will have some "aha" moments after reading some of the posts.

I have included my logo files

```html
<!DOCTYPE html>
<html lang="en">
<head>
<meta charset="utf-8">
<title>The Wandering Mentor</title>
<link rel="stylesheet" href="https://fonts.googleapis.com/css2?family=Bebas+Neue&family=Noto+Serif:wght@400;700&family=Poppins:wght@300;400;500&display=swap">
<style>
:root{
  --gold:#d8aa66;
  --gold-soft:#ddb57d;
  --ink:#1c1c1c;
  --text:#555;
  --beige:#f7f0e3;
  --dark:#2b2723;
  --darker:#1f1d1b;
  --white:#fff;
}
*{box-sizing:border-box;margin:0;padding:0}
html,body{width:1200px;height:4812px;overflow:hidden}
body{position:relative;font-family:'Poppins',sans-serif;color:var(--text);background:var(--white)}
.abs{position:absolute}

/* top bar */
.topbar{left:0;top:0;width:1200px;height:37px;background:var(--darker);color:#ddd;font-size:11px}
.topbar .follow{position:absolute;left:60px;top:11px}
.topbar .dot{position:absolute;top:13px;width:11px;height:11px;border-radius:50%;background:var(--gold)}
.topbar .contact{position:absolute;top:11px;display:flex;align-items:center;gap:8px}

/* nav */
.nav{left:0;top:37px;width:1200px;height:75px;background:var(--white);font-size:12px;color:#333}
.nav a{position:absolute;top:28px;color:#333;text-decoration:none}
.brand{position:absolute;left:510px;top:6px;width:180px;text-align:center}
.brand .mark{width:40px;height:40px;border-radius:50%;border:2px solid var(--gold);margin:0 auto 4px}
.brand .name{font-size:15px;color:#222}
.search{position:absolute;left:1104px;top:20px;width:34px;height:34px;border:2px solid #222;border-radius:50%}

/* hero */
.hero{left:0;top:112px;width:1200px;height:693px;
  background:
    radial-gradient(ellipse 520px 360px at 28% 38%,rgba(122,70,36,.85) 0%,rgba(122,70,36,0) 70%),
    radial-gradient(ellipse 300px 300px at 78% 55%,rgba(70,72,60,.8) 0%,rgba(70,72,60,0) 70%),
    linear-gradient(180deg,#2f3b22 0%,#3f4a2a 30%,#5a4a30 55%,#6e5d40 70%,#d9d6cf 86%,#fff 100%)}
.hero h1{position:absolute;left:0;top:140px;width:1200px;text-align:center;font-family:'Bebas Neue',sans-serif;font-weight:400;font-size:56px;line-height:64px;color:var(--white);letter-spacing:1px}
.hero h1 .accent{color:var(--gold)}
.newsletter{left:224px;top:673px;width:750px;height:88px;background:var(--gold-soft);border-radius:14px}
.newsletter .label{position:absolute;left:30px;top:16px;font-family:'Noto Serif',serif;font-size:23px;line-height:26px;color:var(--white);text-align:center}
.field{position:absolute;background:var(--white);border-radius:6px;font-size:11px;color:#666;padding:11px 14px;height:38px;font-family:'Noto Serif',serif}
.btn-dark{position:absolute;background:var(--ink);color:var(--white);font-family:'Noto Serif',serif;font-weight:700;font-size:14px;border-radius:8px;text-align:center;letter-spacing:.5px}

/* welcome */
.welcome .eyebrow{left:157px;top:872px;font-family:'Noto Serif',serif;font-size:14px;color:var(--gold)}
.welcome h2{left:155px;top:900px;font-family:'Noto Serif',serif;font-size:34px;line-height:42px;color:var(--ink);font-weight:700}
.welcome p{left:155px;width:410px;font-size:11px;line-height:21px;color:#555}
.welcome .portrait{left:691px;top:852px;width:360px;height:360px;border-radius:50%;
  background:
    radial-gradient(ellipse 200px 80px at 55% 28%,#4f6a34 0%,rgba(79,106,52,0) 80%),
    linear-gradient(180deg,#b9cde0 0%,#a7b8a0 22%,#5f7040 34%,#c9b99a 45%,#d8c9ab 75%,#c6b495 100%)}

/* news */
.news{left:0;top:1290px;width:1200px;height:585px;background:var(--beige)}
.section-title{position:absolute;left:0;width:1200px;text-align:center;font-family:'Noto Serif',serif;font-size:34px;color:var(--ink);font-weight:400}
.news-card{position:absolute;top:1426px;width:260px;height:374px;background:var(--white)}
.news-card .img{height:187px}
.news-card .date{position:absolute;left:15px;top:210px;font-size:11px;color:var(--gold)}
.news-card h3{position:absolute;left:15px;top:236px;width:235px;font-family:'Noto Serif',serif;font-size:13.5px;line-height:20px;color:var(--ink);font-weight:700}
.news-card p{position:absolute;left:15px;top:285px;width:230px;font-size:11px;line-height:20px;color:#666}

/* events */
.events-photo{left:0;top:2093px;width:542px;height:453px;
  background:
    radial-gradient(ellipse 300px 330px at 62% 72%,#6a4528 0%,#5a3a22 45%,rgba(90,58,34,0) 80%),
    radial-gradient(ellipse 160px 120px at 26% 40%,rgba(60,45,35,.55) 0%,rgba(60,45,35,0) 80%),
    linear-gradient(180deg,#ffffff 0%,#f3efea 55%,#8a6a4c 100%)}
.events-title{left:648px;top:1945px;font-family:'Noto Serif',serif;font-size:34px;color:var(--ink)}
.event{position:absolute;left:648px;width:434px;height:110px;border:1.5px dashed var(--gold);border-radius:18px;background:var(--white)}
.event .img{position:absolute;left:6px;top:6px;width:120px;height:96px;border-radius:12px}
.event .cat{position:absolute;left:148px;top:18px;font-size:13px;color:var(--gold)}
.event h3{position:absolute;left:148px;top:42px;width:210px;font-family:'Noto Serif',serif;font-size:15px;line-height:22px;color:var(--ink);font-weight:700}
.event .btn-dark{left:370px;top:33px;width:121px;height:40px;line-height:40px;border-radius:10px}
.explore{left:664px;top:2440px;font-family:'Noto Serif',serif;font-size:14px;color:var(--gold);text-decoration:underline}

/* horsemanship */
.horse{left:0;top:2546px;width:1200px;height:676px;background:linear-gradient(180deg,#2a2622 0%,#332d27 50%,#2a2622 100%)}
.horse .section-title{color:var(--white);top:68px}
.horse .img{position:absolute;left:314px;top:149px;width:570px;height:277px;
  background:
    radial-gradient(ellipse 150px 130px at 72% 62%,#7a4a2a 0%,rgba(122,74,42,0) 80%),
    radial-gradient(ellipse 50px 40px at 22% 88%,#b8323a 0%,rgba(184,50,58,0) 90%),
    linear-gradient(180deg,#8aa3bb 0%,#a9b4b5 30%,#8a7358 50%,#b59c78 75%,#a88a63 100%)}
.horse p{position:absolute;left:314px;top:455px;width:570px;text-align:center;font-size:12px;line-height:21px;color:#e4e0da}
.btn-gold{position:absolute;background:var(--gold-soft);color:var(--white);font-family:'Noto Serif',serif;font-size:14px;text-align:center;border-radius:12px;letter-spacing:.5px}

/* advise */
.advise-card{position:absolute;top:3370px;width:316px;height:164px;border:1.5px solid #777;background:var(--white)}
.advise-card .img{position:absolute;left:2px;top:18px;width:108px;height:126px}
.advise-card .cat{position:absolute;left:125px;top:16px;font-family:'Noto Serif',serif;font-size:11px;color:var(--gold)}
.advise-card h3{position:absolute;left:125px;top:36px;width:180px;font-family:'Noto Serif',serif;font-size:13.5px;line-height:20px;color:var(--ink);font-weight:700}
.advise-card p{position:absolute;left:125px;top:86px;width:180px;font-size:10.5px;line-height:18px;color:#666}

/* gallery */
.gallery{left:0;top:3607px;width:1200px;height:770px;background:var(--beige)}
.gallery .section-title{top:70px}
.tile{position:absolute}
.viewall{left:787px;top:4236px;font-family:'Noto Serif',serif;font-size:14px;font-weight:700;color:var(--ink);text-decoration:underline}

/* footer */
.footer{left:0;top:4377px;width:1200px;height:435px;background:linear-gradient(180deg,#2c2824 0%,#24211e 100%);color:#ddd}
.footer h4{position:absolute;font-family:'Noto Serif',serif;font-size:16px;font-weight:400;color:#eee}
.footer ul{position:absolute;left:62px;top:88px;list-style:none;font-size:11px;line-height:24px;color:#ddd}
.ffield{position:absolute;height:36px;border:1px solid #888;background:var(--white);font-size:10.5px;color:#555;padding:10px 14px}
.hex{position:absolute;width:44px;height:44px}
.copy{left:0;top:4782px;width:1200px;text-align:center;font-size:10.5px;color:#ddd}
.copy span{color:var(--gold)}
</style>
</head>
<body>

<div class="abs topbar">
  <span class="follow">Follow Us :</span>
  <span class="dot" style="left:136px"></span>
  <span class="dot" style="left:160px"></span>
  <span class="dot" style="left:184px"></span>
  <span class="contact" style="left:800px">
    <svg width="14" height="14" viewBox="0 0 24 24"><path fill="#d8aa66" d="M6.6 10.8a15 15 0 0 0 6.6 6.6l2.2-2.2c.3-.3.7-.4 1-.2 1.1.4 2.3.6 3.6.6.6 0 1 .4 1 1V20c0 .6-.4 1-1 1C10.6 21 3 13.4 3 4c0-.6.4-1 1-1h3.5c.6 0 1 .4 1 1 0 1.3.2 2.5.6 3.6.1.3 0 .7-.2 1z"/></svg>
    +1 000 000 0000
  </span>
  <span class="contact" style="left:950px">
    <svg width="16" height="12" viewBox="0 0 16 12"><rect width="16" height="12" rx="1.5" fill="#d8aa66"/><path d="M1 1l7 5 7-5" stroke="#1f1d1b" stroke-width="1.4" fill="none"/></svg>
    info@WanderingMentor.com
  </span>
</div>

<nav class="abs nav">
  <svg class="abs" style="left:210px;top:26px" width="18" height="16" viewBox="0 0 18 16"><path fill="#d8aa66" d="M9 0l9 8h-2.5v8h-4.5v-5h-4v5H2.5V8H0z"/></svg>
  <a style="left:251px">News</a>
  <a style="left:310px">Events</a>
  <a style="left:373px">Gallery</a>
  <a style="left:440px">Advise</a>
  <div class="brand"><div class="mark"></div><div class="name">The Wandering Mentor</div></div>
  <a style="left:730px">Horsemanship</a>
  <a style="left:844px">Dressage</a>
  <a style="left:925px">Contact Us</a>
  <div class="search">
    <svg width="30" height="30" viewBox="0 0 30 30"><circle cx="14" cy="14" r="5.5" stroke="#222" stroke-width="2" fill="none"/><path d="M18 18l4 4" stroke="#222" stroke-width="2"/></svg>
  </div>
</nav>

<section class="abs hero" role="img" aria-label="Rider kneeling beside a bay horse in a wooded paddock, soft mist at the bottom">
  <h1>A place for our thoughts<br>fears, finds, fads<br><span class="accent">obsessions and opinions</span></h1>
</section>
<form class="abs newsletter">
  <div class="label">Newsletter<br>Signup !</div>
  <div class="field" style="left:194px;top:26px;width:202px">Enter Name *</div>
  <div class="field" style="left:404px;top:26px;width:202px">Enter Email *</div>
  <div class="btn-dark" style="left:614px;top:26px;width:120px;height:38px;line-height:38px">SUBSCRIBE</div>
</form>

<section class="welcome">
  <div class="abs eyebrow">Welcome To</div>
  <h2 class="abs">The Wandering<br>Mentor</h2>
  <p class="abs" style="top:998px">I started The Wandering Mentor in 2021 to write about the practice of academic advising through the lens of horsemanship.</p>
  <p class="abs" style="top:1051px">After one year of developing skills as a brand new equestrian, I couldn’t help but notice the similarities between my vocation as an academic advisor and my avocation as a budding equestrian. I hope my musings about my journey in two very different fields will cultivate curiosity, widen your aperture and ignite academic advisors to take their practice to the next level</p>
  <div class="abs portrait" role="img" aria-label="Two riders in hats working with a black horse in a sand arena"></div>
</section>

<section class="abs news"></section>
<h2 class="section-title" style="top:1356px">Latest News</h2>
<svg class="abs" style="left:26px;top:1592px" width="14" height="30" viewBox="0 0 14 30"><path d="M12 1L2 15l10 14" stroke="#333" stroke-width="1.5" fill="none"/></svg>
<svg class="abs" style="left:1162px;top:1592px" width="14" height="30" viewBox="0 0 14 30"><path d="M2 1l10 14-10 14" stroke="#333" stroke-width="1.5" fill="none"/></svg>

<article class="news-card" style="left:60px">
  <div class="img" role="img" aria-label="Horse and rider clearing a blue and white show jump" style="background:radial-gradient(ellipse 70px 60px at 45% 45%,#3a2a22 0%,rgba(58,42,34,0) 85%),linear-gradient(180deg,#c9a43a 0%,#9a9a3c 40%,#7fa0c8 70%,#6d7a3d 100%)"></div>
  <div class="date">September 10, 2021</div>
  <h3>Lorem Ipsum has been the indu standard dummy text ever!</h3>
  <p>Lorem Ipsum has been the industry's standard dummy text ever since the 1500s, when an unknown printe</p>
</article>
<article class="news-card" style="left:334px">
  <div class="img" role="img" aria-label="Rider jumping a log fence in an open field" style="background:radial-gradient(ellipse 60px 55px at 55% 52%,#3b2a20 0%,rgba(59,42,32,0) 85%),linear-gradient(180deg,#8fb0d6 0%,#b4c8dc 25%,#6f9a48 45%,#7d9a4a 75%,#8a7a55 100%)"></div>
  <div class="date">September 10, 2021</div>
  <h3>Lorem Ipsum has been the indu standard dummy text ever!</h3>
  <p>Lorem Ipsum has been the industry's standard dummy text ever since the 1500s, when an unknown printe</p>
</article>
<article class="news-card" style="left:608px">
  <div class="img" role="img" aria-label="Handler standing beside a chestnut horse" style="background:radial-gradient(ellipse 90px 100px at 40% 60%,#7a4424 0%,rgba(122,68,36,0) 85%),linear-gradient(180deg,#4f83bd 0%,#6f98c4 40%,#8a6a4c 75%,#6b4a30 100%)"></div>
  <div class="date">September 10, 2021</div>
  <h3>Lorem Ipsum has been the indu standard dummy text ever!</h3>
  <p>Lorem Ipsum has been the industry's standard dummy text ever since the 1500s, when an unknown printe</p>
</article>
<article class="news-card" style="left:882px">
  <div class="img" role="img" aria-label="Person mounting a paint horse in an arena" style="background:radial-gradient(ellipse 80px 60px at 45% 65%,#5a4a40 0%,rgba(90,74,64,0) 85%),linear-gradient(180deg,#9fb6cf 0%,#c3cfdb 35%,#b0a083 60%,#a38b68 100%)"></div>
  <div class="date">September 10, 2021</div>
  <h3>Lorem Ipsum has been the indu standard dummy text ever!</h3>
  <p>Lorem Ipsum has been the industry's standard dummy text ever since the 1500s, when an unknown printe</p>
</article>

<div class="abs events-photo" role="img" aria-label="Smiling rider in a helmet hugging the neck of a brown horse"></div>
<h2 class="abs events-title">Latest Events</h2>

<div class="event" style="top:2026px">
  <div class="img" role="img" aria-label="Group of riders on horseback" style="background:radial-gradient(ellipse 50px 35px at 50% 70%,#4a3a30 0%,rgba(74,58,48,0) 85%),linear-gradient(180deg,#b9c4cc,#8a8e86 50%,#6e5e4a)"></div>
  <div class="cat">Horsemanship</div>
  <h3>Lorem Ipsum has been the industry's stan text ever!</h3>
  <div class="btn-dark">SUBSCRIBE</div>
</div>
<div class="event" style="top:2162px">
  <div class="img" role="img" aria-label="Riders on a trail through green trees" style="background:radial-gradient(ellipse 50px 35px at 50% 70%,#6b3a2a 0%,rgba(107,58,42,0) 85%),linear-gradient(180deg,#2f4a22,#4a6a30 50%,#5e4a30)"></div>
  <div class="cat">Horsemanship</div>
  <h3>Lorem Ipsum has been the industry's stan text ever!</h3>
  <div class="btn-dark">SUBSCRIBE</div>
</div>
<div class="event" style="top:2298px">
  <div class="img" role="img" aria-label="Rider with arms raised beside a horse at sunset" style="background:radial-gradient(ellipse 50px 40px at 50% 75%,#6a3a22 0%,rgba(106,58,34,0) 85%),linear-gradient(180deg,#f0b66a,#d98a44 50%,#7b4b2c)"></div>
  <div class="cat">Horsemanship</div>
  <h3>Lorem Ipsum has been the industry's stan text ever!</h3>
  <div class="btn-dark">SUBSCRIBE</div>
</div>
<a class="abs explore">Explore All</a>

<section class="abs horse">
  <h2 class="section-title">Horsemanship</h2>
  <div class="img" role="img" aria-label="Cowboy riding a bay horse around a barrel beside a wooden fence"></div>
  <p>Lorem Ipsum has been the industry's standard dummy text ever since the 1500s, when an unknown printer took a galley of type and scrambled it to make a type specimen book. It has survived not only five centuries, but also the leap into electronic typesetting, remaining essentially unchanged. It was popularised in the 1960s.</p>
  <div class="btn-gold" style="left:529px;top:562px;width:142px;height:40px;line-height:40px">LEARN MORE</div>
</section>

<h2 class="section-title" style="top:3290px">Advise</h2>
<article class="advise-card" style="left:105px">
  <div class="img" role="img" aria-label="Two riders with a horse in a sand arena" style="background:radial-gradient(ellipse 30px 30px at 50% 55%,#2a2a2a 0%,rgba(42,42,42,0) 85%),linear-gradient(180deg,#a9c0d6 0%,#6f8a48 30%,#c8b796 55%,#bda986 100%)"></div>
  <div class="cat">Academic Advisor</div>
  <h3>Lorem Ipsum has the been the typeing</h3>
  <p>Lorem Ipsum has been the industry's standard dummy text ever since the.</p>
</article>
<article class="advise-card" style="left:441px">
  <div class="img" role="img" aria-label="Rider on a chestnut horse in an arena" style="background:radial-gradient(ellipse 40px 40px at 50% 60%,#7a4424 0%,rgba(122,68,36,0) 85%),linear-gradient(180deg,#9fb6cc 0%,#8a9a7a 35%,#a8906c 65%,#9c8060 100%)"></div>
  <div class="cat">Academic Advisor</div>
  <h3>Lorem Ipsum has the been the typeing</h3>
  <p>Lorem Ipsum has been the industry's standard dummy text ever since the.</p>
</article>
<article class="advise-card" style="left:778px">
  <div class="img" role="img" aria-label="Person swinging a rope beside a horse outdoors" style="background:radial-gradient(ellipse 30px 40px at 45% 55%,#2f5a9a 0%,rgba(47,90,154,0) 85%),linear-gradient(180deg,#7fa6cc 0%,#a9c0d2 30%,#5a8a3c 60%,#4f7a3c 100%)"></div>
  <div class="cat">Academic Advisor</div>
  <h3>Lorem Ipsum has the been the typeing</h3>
  <p>Lorem Ipsum has been the industry's standard dummy text ever since the.</p>
</article>

<section class="abs gallery"><h2 class="section-title">Gallery</h2></section>
<div class="tile" role="img" aria-label="Rider on a dark horse in a green field" style="left:245px;top:3889px;width:146px;height:135px;background:radial-gradient(ellipse 45px 40px at 50% 55%,#2a2320 0%,rgba(42,35,32,0) 85%),linear-gradient(180deg,#4f6a32,#5f7a3e 60%,#3b4a26)"></div>
<div class="tile" role="img" aria-label="Horses being led along a mountain path" style="left:402px;top:3843px;width:174px;height:181px;background:radial-gradient(ellipse 60px 50px at 60% 65%,#5a3a22 0%,rgba(90,58,34,0) 85%),linear-gradient(180deg,#cfd8de 0%,#8a9a9a 30%,#9a8a70 60%,#6e5a43 100%)"></div>
<div class="tile" role="img" aria-label="Two riders on horseback in front of mountains" style="left:585px;top:3764px;width:213px;height:260px;background:radial-gradient(ellipse 90px 70px at 50% 72%,#6b3f22 0%,rgba(107,63,34,0) 85%),linear-gradient(180deg,#8eb2d6 0%,#a8bcc8 30%,#7a8a7a 45%,#8a7458 75%,#6b4d33 100%)"></div>
<div class="tile" role="img" aria-label="Riders on a sunlit forest trail" style="left:809px;top:3889px;width:148px;height:135px;background:radial-gradient(ellipse 50px 50px at 30% 30%,#f2eed0 0%,rgba(242,238,208,0) 85%),linear-gradient(180deg,#8a9a6a,#51653a 60%,#6a5a40)"></div>
<div class="tile" role="img" aria-label="Rider with raised arms beside horses at sunset" style="left:292px;top:4035px;width:147px;height:135px;background:radial-gradient(ellipse 60px 40px at 50% 25%,#f4c27a 0%,rgba(244,194,122,0) 85%),linear-gradient(180deg,#e4a35a,#b86a38 60%,#8a4f2c)"></div>
<div class="tile" role="img" aria-label="Rider in a helmet beside a bay horse" style="left:449px;top:4035px;width:218px;height:262px;background:radial-gradient(ellipse 70px 110px at 35% 55%,#6b3f22 0%,rgba(107,63,34,0) 85%),radial-gradient(ellipse 50px 80px at 75% 70%,#eeeae4 0%,rgba(238,234,228,0) 85%),linear-gradient(180deg,#8fae5c,#7aa04a 50%,#8a8a5a)"></div>
<div class="tile" role="img" aria-label="Cowboy riding a chestnut horse under a blue sky" style="left:678px;top:4035px;width:174px;height:183px;background:radial-gradient(ellipse 70px 55px at 50% 70%,#a55a28 0%,rgba(165,90,40,0) 85%),linear-gradient(180deg,#7fa6cc 0%,#a8c0d6 45%,#b07a48 75%,#8a5a34 100%)"></div>
<a class="abs viewall">View All</a>

<footer class="abs footer">
  <h4 style="left:62px;top:42px">Sitemap</h4>
  <ul><li>News</li><li>Events</li><li>Gallery</li><li>Advise</li><li>Horsemanship</li><li>Dressage</li></ul>

  <h4 style="left:336px;top:42px">Get In Touch With Us ?</h4>
  <div class="abs" style="left:336px;top:88px;font-size:11px">Have an any Question for Contact Us !</div>
  <div class="ffield" style="left:336px;top:123px;width:240px">Name *</div>
  <div class="ffield" style="left:587px;top:123px;width:240px">Email *</div>
  <div class="ffield" style="left:336px;top:172px;width:240px">Phone *</div>
  <div class="ffield" style="left:587px;top:172px;width:240px">Your Question *</div>
  <div class="ffield" style="left:336px;top:217px;width:491px;height:68px">Message *</div>
  <div class="btn-gold" style="left:335px;top:297px;width:108px;height:36px;line-height:36px;border-radius:10px;font-weight:700">SUBMIT</div>

  <h4 style="left:886px;top:42px">Contact Us</h4>
  <svg class="hex" style="left:884px;top:98px" viewBox="0 0 44 44"><path d="M22 2l18 10v20L22 42 4 32V12z" fill="#d8aa66"/><path d="M22 12a6 6 0 0 0-6 6c0 5 6 12 6 12s6-7 6-12a6 6 0 0 0-6-6zm0 8a2 2 0 1 1 0-4 2 2 0 0 1 0 4z" fill="#fff"/></svg>
  <div class="abs" style="left:948px;top:100px;font-family:'Noto Serif',serif;font-size:15px;color:#eee">The Wandering Mentor</div>
  <div class="abs" style="left:948px;top:124px;width:170px;font-size:10px;line-height:18px">Lorem Ipsum has been this industry's standard text</div>
  <svg class="hex" style="left:884px;top:168px" viewBox="0 0 44 44"><path d="M22 2l18 10v20L22 42 4 32V12z" fill="#d8aa66"/><path d="M17 15c1 5 5 10 11 12l2-2-3-3-2 1c-2-1-4-3-5-5l1-2-3-3z" fill="#fff"/></svg>
  <div class="abs" style="left:950px;top:175px;font-size:21px;color:#eee">+1 000 000 0000</div>
  <svg class="hex" style="left:884px;top:238px" viewBox="0 0 44 44"><path d="M22 2l18 10v20L22 42 4 32V12z" fill="#d8aa66"/><rect x="13" y="16" width="18" height="13" rx="1.5" fill="#fff"/><path d="M14 17l8 6 8-6" stroke="#d8aa66" stroke-width="1.4" fill="none"/></svg>
  <div class="abs" style="left:948px;top:253px;font-size:11px;color:#eee">info@WanderingMentor.com</div>
</footer>
<div class="abs copy">©<span>The Wandering Mentor</span> - 2021 All rights reserved.</div>

</body>
</html>
```